Flyer Design

I need a flyer designed for a new company in Berkshire called 'Gymzo'. It is a personal training business which will operate from a personal / purpose built gym, with the option of training clients in their homes/local parks. I will offer fitness training, advice, nutrition advice. There will also be bootcamps for customers.

Industry/Entity Type

Nutrition

```html
<!DOCTYPE html>
<html lang="en">
<head>
<meta charset="utf-8">
<title>Gymzo — Personal In Home Training</title>
<link rel="stylesheet" href="https://fonts.googleapis.com/css2?family=Oswald:wght@700&family=Open+Sans:wght@700&display=swap">
<style>
  :root {
    --sky-light: #ffffff;
    --sky-tint: #c9f1f5;
    --headline-red: #b3141c;
    --brand-blue: #2b43c8;
    --panel-blue: #2447b8;
    --panel-mid: #1a349a;
    --panel-deep: #0b1a66;
    --copy-white: #ffffff;
    --accent-orange: #f5871f;
    --ink-black: #0c0c0c;
    --skin-light: #d4996f;
    --skin-mid: #b77a55;
    --skin-dark: #8a5336;
  }
  * { margin: 0; padding: 0; box-sizing: border-box; }
  html, body { width: 1200px; height: 851px; overflow: hidden; background: #fff; }
  .flyer {
    position: relative; width: 1200px; height: 851px; overflow: hidden;
    font-family: "Open Sans", Arial, sans-serif; font-weight: 700;
  }
  .header {
    position: absolute; left: 0; top: 0; width: 1200px; height: 265px;
    background: linear-gradient(90deg, var(--sky-light) 0%, var(--sky-tint) 100%);
  }
  .brand {
    position: absolute; left: 40px; top: 78px; width: 460px; text-align: center;
    font-size: 96px; line-height: 1; color: var(--brand-blue);
  }
  .headline {
    position: absolute; left: 500px; top: 22px; width: 660px; text-align: center;
    font-family: "Oswald", Impact, sans-serif; font-weight: 700;
    font-variant: small-caps;
    color: var(--headline-red); font-size: 84px; line-height: 72px;
    letter-spacing: 3px; text-shadow: 3px 3px 4px rgba(0,0,0,.45);
  }
  .offer-panel {
    position: absolute; left: 0; top: 265px; width: 1200px; height: 586px;
    background: radial-gradient(ellipse at 60% 35%, var(--panel-blue) 0%, var(--panel-mid) 45%, var(--panel-deep) 100%);
  }
  .trainer-photo {
    position: absolute; left: 0; top: 265px; width: 520px; height: 586px;
    background: linear-gradient(90deg, var(--skin-dark) 0%, var(--skin-mid) 35%, var(--skin-light) 60%, rgba(183,122,85,.6) 82%, rgba(36,71,184,0) 100%);
  }
  .offer-copy p, .offer-copy h2 {
    position: absolute; text-align: center; color: var(--copy-white); font-weight: 700;
  }
  .services { left: 560px; top: 272px; width: 590px; font-size: 38px; line-height: 46px; }
  .nutrition { left: 560px; top: 372px; width: 600px; font-size: 33px; line-height: 42px; color: var(--accent-orange) !important; }
  .bootcamp-title {
    left: 450px; top: 474px; width: 700px; font-size: 46px; line-height: 56px;
    color: var(--ink-black) !important;
    text-shadow: 1px 1px 0 rgba(255,255,255,.5), 2px 2px 3px rgba(0,0,0,.4);
  }
  .bootcamp-copy { left: 480px; top: 537px; width: 600px; font-size: 25px; line-height: 32px; }
  .contact { left: 470px; top: 718px; width: 700px; font-size: 40px; line-height: 50px; }
  .phone {
    left: 560px; top: 764px; width: 480px; font-size: 42px; line-height: 50px;
    letter-spacing: 7px; color: var(--accent-orange) !important;
  }
</style>
</head>
<body>
  <main class="flyer">
    <header class="header">
      <div class="brand">Gymzo</div>
      <h1 class="headline">Personal In Home<br>Training<br>For Great Results</h1>
    </header>
    <section class="offer-panel"></section>
    <div class="trainer-photo" role="img" aria-label="Photo of a muscular shirtless man holding a spoon and a glass bowl of cereal"></div>
    <section class="offer-copy">
      <p class="services">Body Assessment, Training<br>&amp; Nutritional Advice</p>
      <p class="nutrition">Eat to Grow/Lose/Perform with<br>Tailor Made Nutrition Program</p>
      <h2 class="bootcamp-title">BOOTCAMP for customers</h2>
      <p class="bootcamp-copy">Fun, outdoor fitness training programs<br>for men and women of all fitness levels.<br>You will lose weight and get fitter faster.<br>You will be more motivated to<br>reach your fitness goals.</p>
      <p class="contact">Contact Gymzo on</p>
      <p class="phone">555.014.2093</p>
    </section>
  </main>
</body>
</html>
```